Husband and i just started a new Hotshot trucking company, Its a pick up and delivery service. We own our own 40 foot gooseneck trailer... Called Roadbird Hauling LLC. We are needing some business cards made to help advertise our new company. We are based out of Ft Worth Tx. We are the ones who transports what ever loads to where ever they need to go, at any time. We stride for success. And we wont take no for an answer.
What we need on there is the following: need it to be all caps please.

DOUGLAS PRATHER "BO"
555-318-4426
ROADBIRDHAULINGLLC@MAILNEST.EXAMPLE

SHELBY CORWIN
555-604-7153

We have a couple logos already made. however we are always game to see new ideas. Thank you for your time.

Target Market(s)

Youth, middle aged. Home buyers

Industry/Entity Type

Hotshot Trucking Pick up and Delivery Service

Contact Information for Business Card

DOUGLAS PRATHER "BO" 555-318-4426 ROADBIRDHAULINGLLC@MAILNEST.EXAMPLE SHELBY CORWIN 555-604-7153 ROADBIRDHAULINGLLC@MAILNEST.EXAMPLE

Font styles to use
Serif
Script

Colors
0054AA
0677BA
7BADD7
CADEEF
E8F1F8
0094D4
00A9DD
6FCCEA
C7EBF8
E9F6FB

Requirements
Must have
• Our company logo. and look one of a kind. also has to be able to catch some ones eye and stand out
Nice to have
• open for ideas..

```html
<!DOCTYPE html>
<html lang="en">
<head>
<meta charset="utf-8">
<title>Roadbird Hauling LLC – Business Cards</title>
<link href="https://fonts.googleapis.com/css2?family=Montserrat:wght@300;400;700;800&display=swap" rel="stylesheet">
<style>
  :root {
    --stage: #2b2c2d;
    --card-white: #fbfbfb;
    --card-black: #0a0d0d;
    --name-blue: #2aaee4;
    --ink: #111111;
    --detail-grey: #6f6f6f;
    --brand-red: #d0242b;
    --brand-white: #f2f2f2;
    --brand-blue: #1d6fd0;
  }
  * { margin: 0; padding: 0; box-sizing: border-box; }
  html, body {
    width: 1200px; height: 1200px; overflow: hidden;
    background: var(--stage);
    font-family: "Montserrat", sans-serif;
  }
  .stage {
    position: relative; width: 1200px; height: 1200px;
  }

  /* Front card (portrait) */
  .card-front {
    position: absolute; left: 110px; top: 250px;
    width: 410px; height: 700px;
    background: var(--card-white);
    box-shadow: 0 18px 40px rgba(0,0,0,.55);
    display: flex; flex-direction: column; align-items: center;
    padding: 70px 24px 60px;
    text-align: center;
  }
  .brand-lockup {
    display: flex; align-items: center; gap: 12px;
    margin-bottom: 58px;
  }
  .brand-dot {
    width: 26px; height: 26px; border-radius: 50%;
    background: var(--brand-blue);
  }
  .brand-name {
    font-weight: 800; font-size: 27px; letter-spacing: .5px;
    line-height: 1.1; color: var(--brand-blue); text-align: left;
  }
  .contact { display: flex; flex-direction: column; align-items: center; }
  .contact-name {
    font-weight: 700; font-size: 24px; color: var(--name-blue);
    letter-spacing: .3px; text-transform: uppercase;
  }
  .contact-icons { display: flex; gap: 6px; margin: 14px 0 12px; }
  .contact-icons svg { width: 24px; height: 24px; display: block; }
  .contact-phone, .contact-email {
    font-weight: 300; color: var(--detail-grey); text-transform: uppercase;
  }
  .contact-phone { font-size: 17px; letter-spacing: 1px; }
  .contact-email { font-size: 13px; letter-spacing: .3px; margin-top: 10px; }
  .divider {
    width: 26px; height: 3px; background: var(--ink);
    margin: 30px 0 34px;
  }

  /* Back card (landscape) */
  .card-back {
    position: absolute; left: 560px; top: 250px;
    width: 600px; height: 343px;
    background: radial-gradient(ellipse at 40% 35%, #151a1a 0%, var(--card-black) 70%);
    box-shadow: 0 18px 40px rgba(0,0,0,.55);
    display: flex; align-items: center; justify-content: space-around;
    padding: 0 30px;
  }
  .back-lockup {
    display: flex; align-items: center; gap: 10px;
  }
  .back-lockup .brand-dot { width: 20px; height: 20px; }
  .back-lockup .brand-name { font-size: 22px; }
  .back-lockup.is-red .brand-dot { background: var(--brand-red); }
  .back-lockup.is-red .brand-name { color: var(--brand-red); }
  .back-lockup.is-white .brand-dot { background: var(--brand-white); }
  .back-lockup.is-white .brand-name { color: var(--brand-white); }
</style>
</head>
<body>
<main class="stage">

  <section class="card-front" aria-label="Business card front">
    <div class="brand-lockup">
      <span class="brand-dot"></span>
      <span class="brand-name">ROADBIRD<br>HAULING LLC</span>
    </div>

    <div class="contact">
      <p class="contact-name">DOUGLAS PRATHER "BO"</p>
      <div class="contact-icons">
        <svg viewBox="0 0 24 24" aria-label="Phone"><circle cx="12" cy="12" r="12" fill="#111"/><path d="M8.2 6.5l2 2.2-1.1 1.4c.8 1.7 2 2.9 3.7 3.8l1.4-1.1 2.2 2-1 1.9c-4.3-.4-8-4.1-8.3-8.4z" fill="#fff"/></svg>
        <svg viewBox="0 0 24 24" aria-label="Email"><circle cx="12" cy="12" r="12" fill="#111"/><rect x="6" y="8" width="12" height="8.5" rx="1" fill="#fff"/><path d="M6.5 8.5L12 13l5.5-4.5" fill="none" stroke="#111" stroke-width="1.2"/></svg>
      </div>
      <p class="contact-phone">555-318-4426</p>
      <p class="contact-email">ROADBIRDHAULINGLLC@MAILNEST.EXAMPLE</p>
    </div>

    <div class="divider"></div>

    <div class="contact">
      <p class="contact-name">SHELBY CORWIN</p>
      <div class="contact-icons">
        <svg viewBox="0 0 24 24" aria-label="Phone"><circle cx="12" cy="12" r="12" fill="#111"/><path d="M8.2 6.5l2 2.2-1.1 1.4c.8 1.7 2 2.9 3.7 3.8l1.4-1.1 2.2 2-1 1.9c-4.3-.4-8-4.1-8.3-8.4z" fill="#fff"/></svg>
        <svg viewBox="0 0 24 24" aria-label="Email"><circle cx="12" cy="12" r="12" fill="#111"/><rect x="6" y="8" width="12" height="8.5" rx="1" fill="#fff"/><path d="M6.5 8.5L12 13l5.5-4.5" fill="none" stroke="#111" stroke-width="1.2"/></svg>
      </div>
      <p class="contact-phone">555-604-7153</p>
      <p class="contact-email">ROADBIRDHAULINGLLC@MAILNEST.EXAMPLE</p>
    </div>
  </section>

  <section class="card-back" aria-label="Business card back">
    <div class="back-lockup is-red">
      <span class="brand-dot"></span>
      <span class="brand-name">ROADBIRD<br>HAULING LLC</span>
    </div>
    <div class="back-lockup is-white">
      <span class="brand-dot"></span>
      <span class="brand-name">ROADBIRD<br>HAULING LLC</span>
    </div>
  </section>

</main>
</body>
</html>
```